Refresh of Business Card Design

Want to refresh the business card design with the new logo while adhering to style guide as attached. Would like to match feel of website www.durmackvinex.com

```html
<!DOCTYPE html>
<html lang="en">
<head>
<meta charset="utf-8">
<title>Durmack Vinex — Business Card Options</title>
<link href="https://fonts.googleapis.com/css2?family=Work+Sans:wght@400;500;600;800&display=swap" rel="stylesheet">
<style>
  :root {
    --navy: #121a28;
    --crimson: #e92246;
    --white: #ffffff;
    --ink: #1a1a1f;
    --silver-light: #e9eaec;
    --silver-dark: #3c4350;
    --sheet: #ffffff;
  }
  * { box-sizing: border-box; margin: 0; padding: 0; }
  html, body {
    width: 975px; height: 1200px; overflow: hidden;
    background: var(--sheet);
    font-family: "Work Sans", Arial, sans-serif;
  }
  .sheet { position: relative; width: 975px; height: 1200px; }

  .card {
    position: absolute; left: 197px;
    width: 582px; height: 356px;
    background: var(--navy);
    overflow: hidden;
  }
  .card--plain { top: 155px; }
  .card--railed { top: 689px; }

  .card__band {
    position: absolute; left: 0; top: 129px;
    width: 100%; height: 86px;
    background: var(--crimson);
  }
  .card__rail { position: absolute; height: 5px; }
  .card__rail--top {
    top: 122px; left: 230px; right: 0;
    background: linear-gradient(90deg, var(--silver-dark), var(--silver-light));
  }
  .card__rail--bottom {
    top: 215px; left: 0; width: 492px;
    background: linear-gradient(90deg, var(--silver-light), var(--silver-dark) 85%, transparent);
  }

  .brand-mark {
    position: absolute; left: 21px; top: 129px;
    width: 282px; height: 86px;
    display: flex; align-items: center; justify-content: center;
    color: var(--white);
    font-weight: 500; font-size: 21px; letter-spacing: 1.5px;
  }

  .wordmark {
    position: absolute; right: 36px; top: 28px;
    text-align: right; color: var(--crimson);
    font-weight: 600; line-height: 0.8;
  }
  .wordmark__upper { display: block; font-size: 51px; letter-spacing: 0.5px; }
  .wordmark__lower { display: block; font-size: 51px; margin-top: 4px; }

  .person {
    position: absolute; right: 36px; top: 150px;
    text-align: right;
  }
  .person__name {
    display: block; color: var(--white);
    font-weight: 800; font-size: 24px; line-height: 1;
  }
  .person__role {
    display: block; color: var(--ink);
    font-weight: 400; font-size: 16px; margin-top: 9px; line-height: 1;
  }

  .contact {
    position: absolute; right: 36px; top: 252px;
    list-style: none; text-align: right;
    color: var(--white);
    font-weight: 400; font-size: 16.5px; line-height: 19.6px;
    letter-spacing: 0.2px;
  }
</style>
</head>
<body>
<main class="sheet">

  <section class="card card--plain">
    <div class="card__band"></div>
    <div class="brand-mark">DURMACK VINEX</div>
    <h1 class="wordmark"><span class="wordmark__upper">DURMACK</span><span class="wordmark__lower">vinex</span></h1>
    <p class="person"><span class="person__name">Reid Calloway</span><span class="person__role">Sales</span></p>
    <ul class="contact">
      <li>Cell : 555.201.4378</li>
      <li>P.O.Box 40215 Carver, TX 79540</li>
      <li>274 Ridgeline Dr Alton. Texas 79230</li>
      <li>www.durmackvinex.com</li>
    </ul>
  </section>

  <section class="card card--railed">
    <div class="card__rail card__rail--top"></div>
    <div class="card__band"></div>
    <div class="card__rail card__rail--bottom"></div>
    <div class="brand-mark">DURMACK VINEX</div>
    <h1 class="wordmark"><span class="wordmark__upper">DURMACK</span><span class="wordmark__lower">vinex</span></h1>
    <p class="person"><span class="person__name">Reid Calloway</span><span class="person__role">Sales</span></p>
    <ul class="contact">
      <li>Cell : 555.201.4378</li>
      <li>P.O.Box 40215 Carver, TX 79540</li>
      <li>274 Ridgeline Dr Alton. Texas 79230</li>
      <li>www.durmackvinex.com</li>
    </ul>
  </section>

</main>
</body>
</html>
```